It must be unique & Proffessional
VORNA GROUP
# 130 Very nice, could you please use the “symbols” for Phone, cellphone and so on, instead of writing “p:” and “c:”. You did that by # 69 :-)
Thanks for all your very creative suggestions.
A general comment:
- Please correct the “projektchef” to “Direktør”
- Please add at fixed telephone number +45 62 18 37 51
- Please add “+45” in front of the cellphone number
- Please make the envelope as window envelops, and logo bottom right corner
- On the A4 paper, we need the logo in top right corner
#61,Very good design, please make the backside as you’ve done by #64
#128Please leave the bottom of the paper free of text and colors, and add only one thin line 13 mm from the page bottom.
Again very good designs, thank you very much
Logo AI file is now uploaded :-)
Now we have our Logo ready, looking forward to see your suggestions for design :-)
TK/RWF Team
Logo is currently being designed, you can participate if you would like to :-)

```html
<!DOCTYPE html>
<html lang="en">
<head>
<meta charset="utf-8">
<title>Vorna Group – Business Card</title>
<link href="https://fonts.googleapis.com/css2?family=Open+Sans:wght@400;600;700;800&display=swap" rel="stylesheet">
<style>
  :root {
    --stage: #ece9e6;
    --card: #ffffff;
    --ink: #3a3a3c;
    --muted: #8a8a8c;
    --rule: #c9c9cb;
    --red: #c4161c;
    --red-dark: #8f0d12;
    --red-light: #d9262c;
  }
  * { box-sizing: border-box; margin: 0; padding: 0; }
  html, body { width: 1200px; height: 758px; overflow: hidden; }
  body {
    background: var(--stage);
    font-family: "Open Sans", Arial, sans-serif;
    color: var(--ink);
    position: relative;
  }
  .card {
    position: absolute;
    width: 500px;
    height: 310px;
    background: var(--card);
    border-radius: 22px;
    box-shadow: 0 6px 18px rgba(0,0,0,0.18);
    overflow: hidden;
  }
  .card--front { left: 70px; top: 200px; }
  .card--back { left: 630px; top: 250px; }

  .brand {
    display: flex;
    align-items: center;
    justify-content: center;
    gap: 10px;
  }
  .brand__mark { width: 22px; height: 22px; background: var(--red); }
  .brand__name {
    font-weight: 800;
    color: var(--ink);
    letter-spacing: 0.02em;
  }

  .card--front .brand { position: absolute; top: 52px; left: 0; right: 0; }
  .card--front .brand__name { font-size: 34px; }

  .band-rule {
    position: absolute; left: 0; right: 0; height: 1px; background: var(--rule);
  }
  .band-rule--top { top: 126px; }
  .band-rule--bottom { top: 226px; }

  .band {
    position: absolute;
    left: 0; right: 0; top: 132px; height: 88px;
    background: linear-gradient(180deg, var(--red-light) 0%, var(--red) 55%, var(--red-dark) 100%);
    display: flex;
    align-items: center;
    justify-content: center;
    color: #fff;
    font-size: 12px;
    line-height: 1.5;
  }
  .address { text-align: right; padding-right: 16px; }
  .divider { width: 1px; height: 58px; background: rgba(255,255,255,0.8); }
  .contacts { list-style: none; padding-left: 16px; }
  .contacts li { display: flex; align-items: center; gap: 7px; }
  .contacts svg { width: 10px; height: 10px; fill: #fff; flex: none; }

  .person {
    position: absolute; left: 0; right: 0; top: 244px;
    text-align: center; font-size: 15px;
  }
  .person__name { color: var(--red); font-weight: 700; }
  .person__role { color: var(--muted); font-weight: 400; }

  .card--back .brand { position: absolute; top: 112px; left: 0; right: 0; }
  .card--back .brand__mark { width: 28px; height: 28px; }
  .card--back .brand__name { font-size: 44px; }
  .web {
    position: absolute; left: 0; right: 0; top: 196px;
    text-align: center; font-size: 19px; color: var(--ink); letter-spacing: 0.03em;
  }
</style>
</head>
<body>
  <section class="card card--front">
    <div class="brand">
      <span class="brand__mark"></span>
      <span class="brand__name">VORNA GROUP</span>
    </div>
    <div class="band-rule band-rule--top"></div>
    <div class="band">
      <address class="address" style="font-style:normal">
        Halvorsvej 22<br>7100 Vejle, Denmark
      </address>
      <span class="divider"></span>
      <ul class="contacts">
        <li><svg viewBox="0 0 10 10"><path d="M2 0h2l1 2.5-1.3 1A5 5 0 0 0 6.5 6.3L7.5 5 10 6v2c0 1-1 2-2 2A8 8 0 0 1 0 2c0-1 1-2 2-2z"/></svg>+45 3187 4602</li>
        <li><svg viewBox="0 0 10 10"><path d="M0 1.5h10v7H0zM1 2.5l4 3 4-3" stroke="#c4161c" stroke-width="0.8"/></svg>kr@vornagroup.com</li>
        <li><svg viewBox="0 0 10 10"><circle cx="5" cy="5" r="4.5" fill="none" stroke="#fff" stroke-width="1.2"/><path d="M0.5 5h9M5 0.5v9" stroke="#fff" stroke-width="0.8"/></svg>www.vornagroup.com</li>
      </ul>
    </div>
    <div class="band-rule band-rule--bottom"></div>
    <p class="person"><span class="person__name">Karsten Ravnholt,</span> <span class="person__role">Projektchef</span></p>
  </section>

  <section class="card card--back">
    <div class="brand">
      <span class="brand__mark"></span>
      <span class="brand__name">VORNA GROUP</span>
    </div>
    <p class="web">www.vornagroup.com</p>
  </section>
</body>
</html>
```